New website for a business that provides behaviour analysis

A new website that details the services that are provided around behaviour analysis for people with a disability through TWVA. There also needs to incorporate an about us and a staff page, Plus a referral form that is a google doc.
The business already has a web address that needs to be tailored.
Soft colours are preferred.
Do not have lots of pictures, keep them minimal.
A logo for the business is also needed to be incorporated, and this is a separate project that can be awarded to the website winner.
Website needs to be able to be used on WIX who will be the host for the design.

Target Market(s)

TWVA clients requiring behaviour support clician

Industry/Entity Type

Clinical behaviour support and analysis

Colors
00AB8E
00BBA5
67D7C9
C6EFE9
E9F9F6

Requirements
Must have
• Soft colours, preferable pale turquoise, minimal pictures, clean, sophisticated and classical look

```html
<!DOCTYPE html>
<html lang="en">
<head>
<meta charset="utf-8">
<title>Calmpath Support</title>
<link href="https://fonts.googleapis.com/css2?family=Marcellus&family=Montserrat:wght@400;500;600;700&display=swap" rel="stylesheet">
<style>
:root{
  --teal-deep:#00AB8E;
  --teal:#00BBA5;
  --teal-soft:#67D7C9;
  --teal-pale:#C6EFE9;
  --teal-mist:#E9F9F6;
  --teal-dark:#00806c;
  --ink:#111;
  --body:#333;
  --white:#fff;
}
*{margin:0;padding:0;box-sizing:border-box}
html,body{width:1200px;height:3268px;overflow:hidden}
body{position:relative;background:var(--white);font-family:'Montserrat',sans-serif;color:var(--body)}
.abs{position:absolute}
.serif{font-family:'Marcellus',serif;font-weight:400}
.btn{position:absolute;display:flex;align-items:center;justify-content:center;font-family:'Montserrat',sans-serif;font-weight:700;color:var(--white);letter-spacing:.3px}

/* header */
.site-header{left:0;top:0;width:1200px;height:71px;background:var(--white)}
.brand{font-family:'Montserrat',sans-serif;font-weight:600;color:var(--teal-deep);font-size:21px;letter-spacing:1px;white-space:nowrap}
.nav-link{top:28px;font-size:13.5px;font-weight:500;color:#222;white-space:nowrap}
.nav-active{font-weight:700}
.nav-underline{left:459px;top:68px;width:84px;height:3px;background:var(--teal-deep)}

/* hero */
.hero{left:0;top:71px;width:1200px;height:596px;background:#eeeeee;overflow:hidden}
.hero-photo{left:420px;top:0;width:780px;height:596px;background:linear-gradient(90deg,#eeeeee 0%,#d8cfc4 28%,#b79676 45%,#8a6a55 65%,#7a4b4a 85%,#a09690 100%)}
.hero-fade{left:300px;top:0;width:420px;height:596px;background:linear-gradient(90deg,#eeeeee 30%,rgba(238,238,238,0) 100%)}
.hero-title{left:107px;font-size:43px;line-height:1;white-space:nowrap}
.hero-text{left:111px;top:344px;font-size:16px;line-height:25.5px;color:#222}
.dots{width:14px}

/* about */
.about-photo{left:119px;top:728px;width:536px;height:424px;background:linear-gradient(135deg,#8e9aa0 0%,#6e7b6a 35%,#2e3650 60%,#b9c4d8 100%)}
.about-card{left:578px;top:779px;width:513px;height:333px;background:linear-gradient(135deg,var(--teal-deep),var(--teal));border-radius:60px 50px 0 50px}
.about-card p{color:var(--white)}

/* services */
.services{left:0;top:1214px;width:1200px;height:722px;background:linear-gradient(180deg,#e5f7f4 0%,#dcf3ef 60%,#e3f6f3 100%)}
.section-title{width:1200px;left:0;text-align:center;color:var(--ink);font-size:40px;letter-spacing:1px}
.rule{height:3px;background:var(--ink)}
.featured{left:450px;top:1383px;width:325px;height:464px;background:var(--white);border:1.5px solid var(--teal);border-radius:45px 0 45px 0}
.ring{border-radius:50%;border:1.5px solid #e2ecea}
.circle-photo{border-radius:50%}
.svc-title{width:300px;text-align:center;font-family:'Marcellus',serif;font-size:21px;color:var(--ink);letter-spacing:.6px}
.svc-text{width:270px;text-align:center;font-size:12.5px;line-height:15px;color:#222}

/* team */
.team-card{top:2097px;width:225px;height:297px;border:1.5px solid var(--teal);background:var(--white)}
.team-photo{left:0;top:0;width:100%;height:186px}
.member-name{left:0;width:100%;top:208px;text-align:center;font-weight:700;font-size:14px;color:var(--ink)}
.member-role{left:0;width:100%;top:231px;text-align:center;font-size:12.5px;line-height:16px;color:#222}

/* referral */
.referral{left:0;top:2503px;width:1200px;height:600px}
.referral-text{left:636px;font-size:14.5px;line-height:23px;color:var(--white)}

/* footer */
.foot-link{top:3146px;font-size:14px;font-weight:700;color:#111;white-space:nowrap}
.social{top:3185px;width:25px;height:25px;border-radius:50%;border:1.5px solid var(--teal-deep)}
</style>
</head>
<body>

<header class="abs site-header">
  <div class="abs brand" style="left:93px;top:24px">CALMPATH SUPPORT</div>
  <nav>
    <div class="abs nav-link nav-active" style="left:463px">SERVICES</div>
    <div class="abs nav-link" style="left:591px">ABOUT US</div>
    <div class="abs nav-link" style="left:724px">TEAM</div>
    <div class="abs nav-link" style="left:818px">BLOGS</div>
    <div class="abs nav-link" style="left:925px">CONTACT US</div>
  </nav>
  <div class="abs nav-underline"></div>
</header>

<section class="abs hero">
  <div class="abs hero-photo" role="img" aria-label="Photo of a clinician meeting a client at a desk with a laptop and paperwork"></div>
  <div class="abs hero-fade"></div>
</section>
<svg class="abs dots" style="left:22px;top:298px" width="14" height="76" viewBox="0 0 14 76">
  <circle cx="7" cy="7" r="5.5" fill="#fff" stroke="#bbb"/>
  <path d="M4.5 8.2 7 5.8 9.5 8.2" fill="none" stroke="#666" stroke-width="1.2"/>
  <circle cx="7" cy="23" r="2.6" fill="#fff"/>
  <circle cx="7" cy="33" r="2.6" fill="#f6f6f6"/>
  <circle cx="7" cy="43" r="2.6" fill="#f6f6f6"/>
  <circle cx="7" cy="53" r="2.6" fill="#f6f6f6"/>
  <circle cx="7" cy="69" r="5.5" fill="#fff" stroke="#bbb"/>
  <path d="M4.5 67.8 7 70.2 9.5 67.8" fill="none" stroke="#666" stroke-width="1.2"/>
</svg>
<h1 class="abs hero-title serif" style="top:243px;color:var(--teal-deep)">WELCOME TO</h1>
<h1 class="abs hero-title serif" style="top:289px;color:var(--ink)">BEHAVIOUR ANALYSIS</h1>
<p class="abs hero-text">Lorem ipsum dolor sit amet, consectetur adipiscing elit,<br>sed do eiusmod tempor incididunt ut labore</p>
<div class="btn" style="left:114px;top:420px;width:194px;height:42px;background:var(--teal-deep);font-size:14px">GET STARTED</div>

<div class="abs about-photo" role="img" aria-label="Photo of a support worker and a client laughing together outdoors"></div>
<div class="abs about-card">
  <p class="abs" style="left:77px;top:53px;font-size:13.5px;letter-spacing:.3px">WHO WE ARE</p>
  <h2 class="abs serif" style="left:77px;top:76px;font-size:35px;color:var(--white);letter-spacing:.5px">ABOUT US</h2>
  <p class="abs" style="left:77px;top:130px;width:400px;font-size:12.5px;line-height:23px">Lorem ipsum dolor sit amet, consectetur adipiscing elit, sed do eiusmod tempor incididunt ut labore et dolore magna aliqua. Ut enim ad minim veniam, quis nostrud exercitation ullamco laboris nisi ut aliquip ex ea commodo co</p>
  <div class="btn" style="left:77px;top:243px;width:153px;height:37px;border:1.5px solid var(--white);font-size:13px">LEARN MORE</div>
</div>

<section class="abs services"></section>
<h2 class="abs section-title serif" style="top:1273px">OUR SERVICES</h2>
<div class="abs rule" style="left:583px;top:1326px;width:51px"></div>

<div class="abs featured"></div>

<div class="abs ring" style="left:157px;top:1403px;width:246px;height:246px"></div>
<div class="abs circle-photo" style="left:171px;top:1417px;width:218px;height:218px;background:linear-gradient(135deg,#7d9a63,#6a7f9c,#3c4a6a)" role="img" aria-label="Photo of a smiling boy in a wheelchair outdoors"></div>
<div class="abs ring" style="left:494px;top:1403px;width:246px;height:246px"></div>
<div class="abs circle-photo" style="left:508px;top:1417px;width:218px;height:218px;background:linear-gradient(135deg,#b98a5e,#d6b08a,#7ea08a)" role="img" aria-label="Photo of a woman enjoying a craft activity"></div>
<div class="abs ring" style="left:833px;top:1403px;width:246px;height:246px"></div>
<div class="abs circle-photo" style="left:847px;top:1417px;width:218px;height:218px;background:linear-gradient(135deg,#d39a58,#6e6a4a,#4c6a80)" role="img" aria-label="Photo of a young person laughing in a group"></div>

<h3 class="abs svc-title" style="left:130px;top:1677px">SERVICE TITLE HERE</h3>
<p class="abs svc-text" style="left:145px;top:1712px">Lorem ipsum dolor sit amet, consectetur adipiscing elit, sed do eiusmod tempor incididunt ut labore et dolor</p>
<div class="btn" style="left:216px;top:1768px;width:130px;height:31px;background:var(--teal);font-size:11px">LEARN MORE</div>

<h3 class="abs svc-title" style="left:467px;top:1677px">BEHAVIOUR THERAPY</h3>
<p class="abs svc-text" style="left:482px;top:1712px">Lorem ipsum dolor sit amet, consectetur adipiscing elit, sed do eiusmod tempor incididunt ut labore et dolor</p>
<div class="btn" style="left:552px;top:1772px;width:132px;height:32px;background:#000;font-size:11px">LEARN MORE</div>

<h3 class="abs svc-title" style="left:806px;top:1677px">SERVICE TITLE HERE</h3>
<p class="abs svc-text" style="left:821px;top:1712px">Lorem ipsum dolor sit amet, consectetur adipiscing elit, sed do eiusmod tempor incididunt ut labore et dolor</p>
<div class="btn" style="left:891px;top:1768px;width:132px;height:31px;background:var(--teal);font-size:11px">LEARN MORE</div>

<h2 class="abs section-title serif" style="top:1997px">MEET THE TEAM</h2>
<div class="abs rule" style="left:580px;top:2058px;width:50px"></div>

<div class="abs team-card" style="left:124px">
  <div class="abs team-photo" style="background:linear-gradient(180deg,#5f5f5f,#8a8a8a)" role="img" aria-label="Portrait of a team member"></div>
  <div class="abs member-name">MEMBER NAME</div>
  <div class="abs member-role">Lorem ipsum dolor sit amet,<br>consectetur adipiscing</div>
</div>
<div class="abs team-card" style="left:369px">
  <div class="abs team-photo" style="background:linear-gradient(180deg,#b9b9bb,#d8d8da)" role="img" aria-label="Portrait of a team member"></div>
  <div class="abs member-name">MEMBER NAME</div>
  <div class="abs member-role">Lorem ipsum dolor sit amet,<br>consectetur adipiscing</div>
</div>
<div class="abs team-card" style="left:616px">
  <div class="abs team-photo" style="background:linear-gradient(180deg,#535a60,#4c6a78)" role="img" aria-label="Portrait of a team member"></div>
  <div class="abs member-name">MEMBER NAME</div>
  <div class="abs member-role">Lorem ipsum dolor sit amet,<br>consectetur adipiscing</div>
</div>
<div class="abs team-card" style="left:860px">
  <div class="abs team-photo" style="background:linear-gradient(180deg,#e4e4e4,#f0eeea)" role="img" aria-label="Portrait of a team member"></div>
  <div class="abs member-name">MEMBER NAME</div>
  <div class="abs member-role">Lorem ipsum dolor sit amet,<br>consectetur adipiscing</div>
</div>
<div class="btn" style="left:520px;top:2425px;width:165px;height:41px;background:var(--teal);font-size:13px">VIEW ALL TEAM</div>

<svg class="abs referral" viewBox="0 0 1200 600" width="1200" height="600">
  <path d="M0 0H1200V480C1080 540 900 590 700 578C450 565 250 530 0 545Z" fill="#7fdccf"/>
  <path d="M0 0H1200V466C1060 530 880 575 690 560C460 545 250 520 0 537Z" fill="var(--teal)"/>
  <circle cx="322" cy="262" r="224" fill="#20d0c0"/>
</svg>
<div class="abs circle-photo" style="left:122px;top:2563px;width:430px;height:430px;background:linear-gradient(135deg,#e8e6e2 0%,#cfcac4 40%,#5a3a6a 60%,#7a5a6a 100%)" role="img" aria-label="Photo of a facilitator at a whiteboard with a client in a wheelchair"></div>
<h2 class="abs serif" style="left:636px;top:2600px;font-size:35px;color:var(--white);letter-spacing:.5px">REFERRAL FORM</h2>
<div class="abs" style="left:636px;top:2649px;width:52px;height:2px;background:var(--white)"></div>
<p class="abs referral-text" style="top:2672px">Lorem ipsum dolor sit amet, consectetur adipiscing elit,<br>sed do eiusmod tempor incididunt ut labore et dolore<br>magna aliqua. Ut enim ad minim veniam, quis nostrud</p>
<p class="abs referral-text" style="top:2768px">Axercitation ullamco laboris nisi ut aliquip ex ea commodo<br>coLorem ipsum dolor sit amet, consectetur adipiscing elit,<br>sed do eiusmod tempor incididunt ut labor</p>
<div class="btn" style="left:636px;top:2862px;width:161px;height:39px;background:var(--teal-dark);font-size:13px">REFERRAL FORM</div>

<footer>
  <div class="abs brand" style="left:113px;top:3143px">CALMPATH SUPPORT</div>
  <div class="abs foot-link" style="left:438px">SERVICES</div>
  <div class="abs foot-link" style="left:573px">ABOUT US</div>
  <div class="abs foot-link" style="left:714px">WHY US</div>
  <div class="abs foot-link" style="left:838px">BLOGS</div>
  <div class="abs foot-link" style="left:951px">CONTACT US</div>
  <div class="abs social" style="left:120px" aria-label="Social link"></div>
  <div class="abs social" style="left:149px" aria-label="Social link"></div>
  <div class="abs social" style="left:178px" aria-label="Social link"></div>
  <p class="abs" style="left:441px;top:3191px;font-size:12px;color:#333">© 2024 Company Name | All Rights Reserved</p>
</footer>

</body>
</html>
```